Harbourline Blinds & Shutters

It Needs to look classy as my target is the upper end of the blind market
I need a Logo design on front and description on back of what i do:
- Roller Blinds
- Vertical Blinds
- Venetian Blinds
- Plantation Shutters
- Aluminum External Shutters
and contact details
Declan
0418275063
and
Trent
0419852306
Updates
Hi Guys,
Sorry for the no feedback but i was waiting on my logo design. But its done now i have uploaded it. so if you could take a look and send through some designs
Reason: my logo was just finished an i just uploaded it today really dont understand why my deadline has been rached foe my bizcards as it states no deadline. But please extend
Target Market(s)
People that live on the coast and are looking for classy good quality blinds and shutters
Font styles to use
Other font styles liked:
- Copperplate Gothic,open to suggestion
Look and feel
Each slider illustrates characteristics of the customer's brand and the style your logo design should communicate.

```html
<!DOCTYPE html>
<html lang="en">
<head>
<meta charset="utf-8">
<title>Harbourline Blinds &amp; Shutters – Business Card</title>
<link rel="stylesheet" href="https://fonts.googleapis.com/css2?family=Arimo:wght@400;700&display=swap">
<style>
  :root {
    --backdrop: #a4cabf;
    --card-black: #050505;
    --gold-light: #e3bf7a;
    --gold-dark: #c9a15e;
    --brand-red: #e2343a;
    --brand-gold: #c9a86a;
    --ink: #1a1a1a;
    --white: #ffffff;
  }
  html, body {
    margin: 0;
    padding: 0;
    width: 1200px;
    height: 856px;
    overflow: hidden;
    background: var(--backdrop);
    font-family: "Arimo", Arial, sans-serif;
  }
  .sheet {
    position: relative;
    width: 1200px;
    height: 856px;
  }
  .card {
    position: absolute;
    top: 283px;
    width: 500px;
    height: 290px;
    border-radius: 28px;
    box-shadow: 0 14px 30px rgba(0, 0, 0, 0.18);
    overflow: hidden;
  }
  .card--front {
    left: 70px;
    background: var(--card-black);
  }
  .card--back {
    left: 630px;
    background: linear-gradient(160deg, var(--gold-light), var(--gold-dark));
  }
  .brand {
    position: absolute;
    left: 48px;
    top: 92px;
    display: flex;
    align-items: center;
    gap: 16px;
  }
  .brand__mark {
    width: 58px;
    height: 58px;
    background: var(--brand-red);
  }
  .brand__name {
    color: var(--white);
    font-weight: 400;
    font-size: 30px;
    line-height: 1.05;
    letter-spacing: 0.5px;
  }
  .brand__name span {
    display: block;
    font-size: 16px;
    letter-spacing: 2px;
    text-transform: uppercase;
  }
  .contacts {
    position: absolute;
    left: 262px;
    top: 190px;
    font-size: 16px;
    line-height: 1.35;
  }
  .contact {
    display: flex;
    gap: 6px;
    align-items: baseline;
  }
  .contact__name {
    font-weight: 700;
    font-size: 19px;
    text-transform: uppercase;
    min-width: 76px;
  }
  .contact--red { color: var(--brand-red); }
  .contact--gold { color: var(--brand-gold); }
  .services {
    position: absolute;
    left: 36px;
    right: 36px;
    top: 118px;
    color: var(--ink);
    font-size: 16px;
    line-height: 1.3;
    text-align: center;
  }
  .services__sep {
    display: inline-block;
    width: 4px;
    height: 13px;
    margin: 0 6px;
    background: var(--brand-red);
    vertical-align: -1px;
  }
</style>
</head>
<body>
  <main class="sheet">
    <section class="card card--front" aria-label="Card front">
      <div class="brand">
        <div class="brand__mark"></div>
        <div class="brand__name">Harbourline<span>Blinds &amp; Shutters</span></div>
      </div>
      <div class="contacts">
        <div class="contact contact--red"><span class="contact__name">Declan</span><span>- 0418275063</span></div>
        <div class="contact contact--gold"><span class="contact__name">Trent</span><span>- 0419852306</span></div>
      </div>
    </section>
    <section class="card card--back" aria-label="Card back">
      <p class="services">
        Roller Blinds<span class="services__sep"></span>Vertical Blinds<span class="services__sep"></span>Venetian Blinds<br>
        Plantation Shutters<span class="services__sep"></span>Aluminum External Shutters
      </p>
    </section>
  </main>
</body>
</html>
```